Tarn - Stationary Design/Layout

We are a well established clothing design and manufacturing company (Tarn Sourcing) based in London UK, with our own factory in Bangladesh, supplying to many fashion retailers and brands. Our factory has very high environmental and ethical standards with people at its heart. Our quality of garments are second to none.
Our new logo has been proudly developed by the Pixel Guild community last month, we are now in the second phase and need the layout designed for our letterheads, double sided business cards, compliment slip and clothing ticket. Feel as creative as you like, but make sure it looks great!!
***The Logo - the logo design and colour is set and should NOT be changed and stay on a dark grey backround. The logo artwork to use is attached.
***Details to use for the business card:
Dorian Pelham
Direct Line: 020 7946 0158
dorian@tarnsourcing-example.com
Tarn Sourching Ltd.
57 - 59 Hollin Row
Fenwick . Ashcombe
NW9 4QT
Switchboard: 020 7946 0274
Fax: 020 7946 0274
www.tarnsourcing-example.co.uk
***Details to use for the letterhead and compliment slip:
Tarn Sourching Ltd.
57 - 59 Hollin Row
Fenwick . Ashcombe
NW9 4QT
Fax: 020 7946 0274
www.tarnsourcing-example.co.uk
***Details for Swing Ticket:
Size: 12cm height by 5.5cm width
One side need to have just the logo without the 'Sourcing', on the other it needs to stay blank

```html
<!DOCTYPE html>
<html lang="en">
<head>
<meta charset="utf-8">
<title>Tarn Sourcing – Stationery</title>
<link rel="stylesheet" href="https://fonts.googleapis.com/css2?family=PT+Sans:wght@400;700&family=Stardos+Stencil:wght@700&family=Tinos&display=swap">
<style>
  :root{
    --dark:#3d3d3d;
    --blue:#a9dde3;
    --ink:#1e1e1e;
    --paper:#ffffff;
    --stage:#f2f2f2;
    --rule:#bbbbbb;
  }
  *{box-sizing:border-box;margin:0;padding:0}
  html,body{width:900px;height:1200px;overflow:hidden;background:var(--stage)}
  body{position:relative;font-family:"PT Sans",Arial,sans-serif;color:var(--ink)}

  .wordmark{font-family:"PT Sans",Arial,sans-serif;font-weight:400;color:var(--blue);line-height:1;white-space:nowrap}
  .wordmark .sub{display:block;letter-spacing:.18em;text-align:right}

  /* Letterhead */
  .letterhead{position:absolute;left:55px;top:28px;width:793px;height:1142px;background:var(--paper);border:1px solid #e2e2e2}
  .lh-logo{position:absolute;left:0;top:0;width:415px;height:137px;background:var(--dark);padding:18px 18px 0 18px}
  .lh-logo .wordmark{font-size:78px;letter-spacing:.04em}
  .lh-logo .sub{font-size:24px;margin-top:8px}
  .lh-web{position:absolute;left:12px;top:146px;font-size:12px}
  .lh-rule{position:absolute;left:415px;top:142px;right:0;height:17px;background:var(--dark)}
  .lh-details{position:absolute;right:28px;top:42px;width:165px;text-align:right;font-size:9.5px;line-height:1.3}
  .lh-details .company{font-size:14px;font-weight:700;margin-bottom:2px}
  .lh-details hr{border:0;border-top:1px solid var(--rule);margin:6px 0 4px}
  .lh-foot{position:absolute;left:0;right:0;bottom:20px;height:32px;display:flex}
  .lh-foot .blue{width:400px;background:var(--blue)}
  .lh-foot .dark{flex:1;background:var(--dark)}

  /* Business cards */
  .card{position:absolute;background:var(--paper);border:1px solid #d6d6d6;overflow:hidden}
  .contact{font-size:11px;line-height:1.35}
  .contact .company{font-size:15px;font-weight:700}
  .contact hr{border:0;border-top:1px solid var(--rule);margin:4px 0}
  .stencil-name{font-family:"Stardos Stencil","Arial Black",sans-serif;font-weight:700;letter-spacing:.03em;text-transform:uppercase}

  .card-a{left:22px;top:222px;width:405px;height:280px}
  .card-a .logo-block{position:absolute;right:0;top:0;width:225px;height:105px;background:var(--dark);padding:14px 14px 0}
  .card-a .wordmark{font-size:48px}
  .card-a .sub{font-size:14px;margin-top:8px}
  .card-a .person{position:absolute;left:18px;top:70px;font-size:11px;line-height:1.35}
  .card-a .person .name{font-family:"Tinos","Times New Roman",serif;font-size:20px;border-bottom:1px solid var(--rule);padding-bottom:2px;margin-bottom:3px}
  .card-a .contact{position:absolute;left:190px;top:128px}
  .card-a .web{position:absolute;left:22px;bottom:32px;font-size:12px}
  .card-a .band-blue{position:absolute;right:0;bottom:26px;width:145px;height:22px;background:var(--blue)}
  .card-a .band-dark{position:absolute;left:0;right:0;bottom:0;height:26px;background:var(--dark)}

  .card-b{left:440px;top:200px;width:438px;height:285px}
  .card-b .logo-block{position:absolute;left:0;right:0;top:0;height:195px;background:var(--dark);padding:26px 22px 0}
  .card-b .wordmark{font-size:92px}
  .card-b .sub{font-size:25px;margin-top:10px}
  .card-b .web{position:absolute;left:22px;top:205px;font-size:12px}
  .card-b .band-blue{position:absolute;right:0;bottom:0;width:185px;height:30px;background:var(--blue)}

  .card-c{left:290px;top:520px;width:455px;height:280px}
  .card-c .top-band{position:absolute;left:0;right:0;top:0;height:22px;background:var(--blue)}
  .card-c .person{position:absolute;right:40px;top:36px;text-align:right;font-size:10px;line-height:1.3}
  .card-c .person .stencil-name{font-size:18px}
  .card-c .contact{position:absolute;left:90px;top:192px;text-align:right;padding-right:10px;border-right:1px solid var(--rule)}
  .card-c .lines{position:absolute;left:250px;top:195px;font-size:11px;line-height:1.35}
  .card-c .band-dark{position:absolute;left:0;bottom:0;width:260px;height:28px;background:var(--dark)}
  .card-c .band-blue{position:absolute;right:0;bottom:18px;width:195px;height:34px;background:var(--blue)}

  .card-d{left:340px;top:815px;width:425px;height:265px}
  .card-d .top-band{position:absolute;left:0;right:0;top:0;height:24px;background:var(--blue)}
  .card-d .person{position:absolute;right:22px;top:36px;text-align:right;font-size:10px;line-height:1.3}
  .card-d .person .stencil-name{font-size:18px;margin-bottom:4px}
  .card-d .contact{position:absolute;left:24px;top:130px;width:170px;text-align:right}
  .card-d .bottom{position:absolute;left:0;bottom:0;width:100%;height:30px}

  /* Swing ticket */
  .ticket{position:absolute;left:97px;top:652px;width:183px;height:392px;border-radius:14px;border:1px solid #555;
    background:linear-gradient(180deg,#555 0%,#000 30%,#000 70%,#222 100%);overflow:hidden}
  .ticket .logo-band{position:absolute;left:0;right:0;top:170px;height:56px;background:var(--dark);border-top:1px solid #888;border-bottom:1px solid #888;
    display:flex;align-items:center;justify-content:center}
  .ticket .wordmark{font-size:46px}
</style>
</head>
<body>

<section class="letterhead">
  <div class="lh-logo"><div class="wordmark">TARN<span class="sub">SOURCING</span></div></div>
  <div class="lh-details">
    <div class="company">Tarn Sourcing Ltd</div>
    57 - 59 Hollin Row, Fenwick<br>Ashcombe, NW9 4QT
    <hr>
    Switchboard : 020 7946 0274<br>Fax : 020 7946 0274
  </div>
  <div class="lh-web">www.tarnsourcing-example.co.uk</div>
  <div class="lh-rule"></div>
  <div class="lh-foot"><div class="blue"></div><div class="dark"></div></div>
</section>

<article class="card card-a">
  <div class="logo-block"><div class="wordmark">TARN<span class="sub">SOURCING</span></div></div>
  <div class="person">
    <div class="name">Dorian Pelham</div>
    Direct line : 020 7946 0158<br>dorian@tarnsourcing-example.com
  </div>
  <div class="contact">
    <div class="company">Tarn Sourcing Ltd</div>
    57 - 59 Hollin Row, Fenwick<br>Ashcombe, NW9 4QT
    <hr>
    Switchboard : 020 7946 0274<br>Fax : 020 7946 0274
  </div>
  <div class="web">www.tarnsourcing-example.co.uk</div>
  <div class="band-blue"></div>
  <div class="band-dark"></div>
</article>

<article class="card card-b">
  <div class="logo-block"><div class="wordmark">TARN<span class="sub">SOURCING</span></div></div>
  <div class="web">www.tarnsourcing-example.co.uk</div>
  <div class="band-blue"></div>
</article>

<article class="card card-c">
  <div class="top-band"></div>
  <div class="person">
    <div class="stencil-name">Dorian Pelham</div>
    Direct line : 020 7946 0158<br>dorian@tarnsourcing-example.com
  </div>
  <div class="contact">
    <div class="company">Tarn Sourcing Ltd</div>
    57 - 59 Hollin Row, Fenwick<br>Ashcombe, NW9 4QT
  </div>
  <div class="lines">Switchboard : 020 7946 0274<br>Fax : 020 7946 0274</div>
  <div class="band-blue"></div>
  <div class="band-dark"></div>
</article>

<article class="card card-d">
  <div class="top-band"></div>
  <div class="person">
    <div class="stencil-name">Dorian Pelham</div>
    Direct line : 020 7946 0158<br>dorian@tarnsourcing-example.com
  </div>
  <div class="contact">
    <div class="company">Tarn Sourcing Ltd</div>
    57 - 59 Hollin Row, Fenwick<br>Ashcombe, NW9 4QT
    <hr>
    Switchboard : 020 7946 0274<br>Fax : 020 7946 0274
  </div>
  <svg class="bottom" viewBox="0 0 425 30" preserveAspectRatio="none" aria-hidden="true">
    <polygon points="0,0 200,0 225,30 0,30" fill="var(--dark)"/>
    <polygon points="200,0 425,0 425,22 222,22" fill="var(--blue)"/>
  </svg>
</article>

<aside class="ticket">
  <div class="logo-band"><div class="wordmark">TARN</div></div>
</aside>

</body>
</html>
```